Business Card for Wellness Clinic

We need a business card for our new logo. I want it to match the feel of the logo

Target Market(s)

Young professional families looking for holistic health care

Industry/Entity Type

Health And Wellness

Contact Information for Business Card

Our business Name: Brackenfield Health & wellness Centre, our phone #, email address...see attached old business card

Font styles to use
Sans Serif

Colors
33b8a4
cee9f5

Requirements
Must have
• my logo and business name
• Font is "Helvetica Neue LT Std 45 Light" and
• Only for "&" using font "Trajan pro bold"
• Use colors in the logo

```html
<!DOCTYPE html>
<html lang="en">
<head>
<meta charset="utf-8">
<title>Brackenfield Health &amp; Wellness Centre – Business Card</title>
<link href="https://fonts.googleapis.com/css2?family=Roboto:wght@300&display=swap" rel="stylesheet">
<style>
  :root {
    --teal: #33b8a4;
    --teal-deep: #27a393;
    --sky: #cee9f5;
    --sky-deep: #b3dcec;
    --card-back: #f6f6f8;
    --ink: #111111;
    --white: #ffffff;
  }
  * { margin: 0; padding: 0; box-sizing: border-box; }
  html, body { width: 1000px; height: 1200px; overflow: hidden; background: var(--white); }
  body { font-family: "Roboto", "Helvetica Neue", Arial, sans-serif; font-weight: 300; color: var(--ink); }
  .sheet { position: relative; width: 1000px; height: 1200px; overflow: hidden; }
  .backdrop { position: absolute; inset: 0; width: 1000px; height: 1200px; }
  .abs { position: absolute; line-height: 1; white-space: nowrap; }

  /* Front */
  .brand-mark { left: 440px; top: 98px; width: 120px; height: 120px; background: var(--teal); }
  .brand-name { left: 0; width: 1000px; top: 300px; text-align: center; font-size: 38px; color: var(--ink); }
  .doctor-name { left: 420px; width: 510px; top: 446px; text-align: center; font-size: 44px; color: var(--white); }
  .doctor-title { left: 420px; width: 510px; top: 496px; text-align: center; font-size: 36px; color: var(--white); }

  /* Back */
  .back-mark { left: 97px; top: 740px; width: 122px; height: 122px; background: var(--teal); }
  .field { left: 257px; width: 671px; display: flex; align-items: flex-end; font-size: 32px; }
  .field .rule { flex: 1; margin-left: 12px; border-bottom: 2px solid var(--ink); margin-bottom: 2px; }
  .field-date { top: 724px; }
  .field-time { top: 783px; }
  .field-for { top: 841px; }
  .notice { left: 428px; width: 500px; top: 895px; font-size: 19px; line-height: 26px; white-space: normal; text-align: justify; text-align-last: justify; }
  .contact { left: 71px; display: flex; align-items: center; font-size: 30px; }
  .contact .icon { width: 42px; height: 42px; margin-right: 20px; flex: none; }
  .contact-phone { top: 928px; }
  .contact-email { top: 984px; }
  .contact-web { top: 1041px; }
  .contact-address { top: 1098px; }
</style>
</head>
<body>
<main class="sheet">
  <svg class="backdrop" viewBox="0 0 1000 1200" aria-hidden="true">
    <!-- front card -->
    <rect x="0" y="0" width="1000" height="572" fill="var(--white)"/>
    <rect x="0" y="0" width="1000" height="20" fill="var(--teal)"/>
    <polygon points="330,412 1000,412 1000,572 260,572" fill="var(--teal)"/>
    <polygon points="290,530 1000,530 1000,572 260,572" fill="var(--teal-deep)"/>
    <polygon points="0,520 210,520 180,572 0,572" fill="var(--sky)"/>
    <!-- back card -->
    <rect x="0" y="629" width="1000" height="571" fill="var(--card-back)"/>
    <polygon points="0,629 780,629 740,684 0,684" fill="var(--teal)"/>
    <polygon points="0,915 600,915 640,1200 0,1200" fill="var(--sky)"/>
    <rect x="0" y="972" width="560" height="113" fill="var(--sky-deep)"/>
    <polygon points="720,1176 1000,1176 1000,1200 705,1200" fill="var(--teal)"/>
  </svg>

  <section class="card-front">
    <div class="abs brand-mark" aria-hidden="true"></div>
    <div class="abs brand-name">Brackenfield Health &amp; Wellness Centre</div>
    <div class="abs doctor-name">Dr. Maren Holloway, N.D.</div>
    <div class="abs doctor-title">Naturopathic Doctor</div>
  </section>

  <section class="card-back">
    <div class="abs back-mark" aria-hidden="true"></div>
    <div class="abs field field-date"><span>Date:</span><span class="rule"></span></div>
    <div class="abs field field-time"><span>Time:</span><span class="rule"></span></div>
    <div class="abs field field-for"><span>For:</span><span class="rule"></span></div>
    <p class="abs notice">If you are unable to keep your appointment, please provide at least 2 business days notice or full visit fees will apply.</p>

    <div class="abs contact contact-phone">
      <svg class="icon" viewBox="0 0 42 42" aria-hidden="true"><circle cx="21" cy="21" r="21" fill="var(--white)"/><path d="M14 11c1-1 2.5-1 3.2.2l2 3.4c.5.9.3 2-.5 2.6l-1.3 1c1 2.6 3 4.6 5.5 5.6l1-1.3c.6-.8 1.7-1 2.6-.5l3.4 2c1.2.7 1.2 2.2.2 3.2l-1.5 1.5c-1.3 1.3-3.3 1.5-4.9.6C18.6 26.9 15 23.3 12.5 18.2c-.9-1.6-.7-3.6.6-4.9z" fill="var(--teal)"/></svg>
      <span>613-555-0148</span>
    </div>
    <div class="abs contact contact-email">
      <svg class="icon" viewBox="0 0 42 42" aria-hidden="true"><circle cx="21" cy="21" r="21" fill="var(--white)"/><rect x="10" y="14" width="22" height="15" fill="var(--teal)"/><path d="M10 14l11 8 11-8M10 29l8-7M32 29l-8-7" fill="none" stroke="var(--white)" stroke-width="1.6"/></svg>
      <span>mholloway@brackenfieldhwc.example</span>
    </div>
    <div class="abs contact contact-web">
      <svg class="icon" viewBox="0 0 42 42" aria-hidden="true"><circle cx="21" cy="21" r="21" fill="var(--white)"/><circle cx="21" cy="21" r="11" fill="var(--teal)"/><path d="M10 21h22M21 10c-4 4-4 18 0 22M21 10c4 4 4 18 0 22" fill="none" stroke="var(--white)" stroke-width="1.6"/></svg>
      <span>www.brackenfieldhwc.example</span>
    </div>
    <div class="abs contact contact-address">
      <svg class="icon" viewBox="0 0 42 42" aria-hidden="true"><circle cx="21" cy="21" r="21" fill="var(--white)"/><path d="M9 21l12-10 12 10h-3v9h-6v-6h-6v6h-6v-9z" fill="var(--teal)"/></svg>
      <span>48 Linden Ave. W, Suite 305, Kingsport, ON&nbsp;&nbsp;&nbsp;K0L 1X2</span>
    </div>
  </section>
</main>
</body>
</html>
```